Quorvane Capital Modern Business Card

We need a modern business card template designed for Quorvane Capital.
Quorvane Capital is a diversified global cryptocurrency investment fund.

The font under the logo: Hiragino Kaku Gothic Pro

Color Hexcode: Main colors white (ffffff) & teal (188383), we are open to adding #fcca46 as an accent

Target Market(s)

Accredited Investors, high net worth individuals and institutional investors

Industry/Entity Type

Investment

Contact Information for Business Card

Contact Information should contain
Name
main phone +1 720 555 0147
cell
email

Font styles to use
Sans Serif
Other font styles liked:
• Hiragino Kaku Gothic Pro

Requirements
Must have
• would like to have icons that identify the contact information
• include our website: www.quorvanecapital.example
• include our Tagline: Diversified Crypto Investment Funds
Nice to have
• Would like to have a simple back side with the logo (without the words) and plenty of space

```html
<!DOCTYPE html>
<html lang="en">
<head>
<meta charset="utf-8">
<title>Quorvane Capital Business Card</title>
<link rel="stylesheet" href="https://fonts.googleapis.com/css2?family=Noto+Sans+JP:wght@400;500;700&display=swap">
<style>
  :root {
    --teal: #188383;
    --teal-light: #22b4b4;
    --teal-mid: #1c9797;
    --grey-band: #5a5a5a;
    --ink: #1e1e1e;
    --paper: #ffffff;
    --backdrop: #d9d9d9;
  }
  * { box-sizing: border-box; margin: 0; padding: 0; }
  html, body {
    width: 1200px; height: 789px; overflow: hidden;
    background: var(--backdrop);
    font-family: "Noto Sans JP", sans-serif;
  }
  .sheet {
    width: 1200px; height: 789px;
    display: flex; align-items: center; justify-content: center; gap: 40px;
  }
  .card {
    position: relative;
    width: 540px; height: 309px;
    overflow: hidden;
    box-shadow: 0 4px 14px rgba(0,0,0,.18);
  }
  /* Front */
  .card-front { background: var(--paper); }
  .card-front .wave { position: absolute; inset: 0; width: 100%; height: 100%; }
  .brand {
    position: absolute; left: 60px; top: 140px;
    display: flex; align-items: center; gap: 10px;
  }
  .brand-square { width: 16px; height: 16px; background: var(--teal-mid); }
  .brand-name {
    font-size: 15px; font-weight: 400; letter-spacing: 1.5px;
    color: var(--ink); text-transform: uppercase;
  }
  .divider {
    position: absolute; left: 292px; top: 62px;
    width: 1.5px; height: 100px; background: var(--teal);
  }
  .contact { position: absolute; left: 312px; top: 48px; }
  .contact-name {
    font-size: 22px; font-weight: 700; color: var(--teal-mid);
    margin-bottom: 8px;
  }
  .contact-list { list-style: none; }
  .contact-item {
    display: flex; align-items: center; gap: 8px;
    font-size: 12.5px; color: var(--ink); line-height: 21px;
    white-space: nowrap;
  }
  .contact-item svg { width: 14px; height: 14px; flex: none; }
  /* Back */
  .card-back {
    background: linear-gradient(115deg, var(--teal) 0%, var(--teal-light) 45%, var(--teal) 100%);
    display: flex; flex-direction: column; align-items: center; justify-content: center;
    gap: 18px;
  }
  .back-brand {
    font-size: 26px; font-weight: 500; letter-spacing: 3px;
    color: rgba(255,255,255,.8); text-transform: uppercase;
  }
  .tagline { font-size: 13px; color: var(--paper); letter-spacing: .5px; }
</style>
</head>
<body>
<main class="sheet">
  <section class="card card-front" aria-label="Business card front">
    <svg class="wave" viewBox="0 0 540 309" preserveAspectRatio="none" aria-hidden="true">
      <path d="M0,303 Q380,292 540,200 L540,208 Q390,298 0,309 Z" fill="var(--grey-band)"/>
      <path d="M40,309 Q400,302 540,216 L540,309 Z" fill="var(--teal-mid)"/>
    </svg>
    <div class="brand">
      <span class="brand-square"></span>
      <span class="brand-name">Quorvane Capital</span>
    </div>
    <div class="divider"></div>
    <div class="contact">
      <h1 class="contact-name">Daniel Reyes</h1>
      <ul class="contact-list">
        <li class="contact-item">
          <svg viewBox="0 0 24 24" aria-hidden="true"><path fill="var(--teal)" d="M6.6 10.8a15 15 0 0 0 6.6 6.6l2.2-2.2c.3-.3.7-.4 1-.2 1.1.4 2.3.6 3.6.6.6 0 1 .4 1 1V20c0 .6-.4 1-1 1A17 17 0 0 1 3 4c0-.6.4-1 1-1h3.5c.6 0 1 .4 1 1 0 1.3.2 2.5.6 3.6.1.3 0 .7-.2 1z"/></svg>
          +1 720 555 0147
        </li>
        <li class="contact-item">
          <svg viewBox="0 0 24 24" aria-hidden="true"><rect x="2.5" y="5" width="19" height="14" fill="none" stroke="var(--teal)" stroke-width="1.6"/><path d="M2.5 5l9.5 8 9.5-8" fill="none" stroke="var(--teal)" stroke-width="1.6"/></svg>
          info@quorvanecapital.example
        </li>
        <li class="contact-item">
          <svg viewBox="0 0 24 24" aria-hidden="true"><g fill="none" stroke="var(--teal)" stroke-width="1.6"><circle cx="12" cy="12" r="9.5"/><ellipse cx="12" cy="12" rx="4" ry="9.5"/><path d="M2.5 12h19M4 7h16M4 17h16"/></g></svg>
          www.quorvanecapital.example
        </li>
      </ul>
    </div>
  </section>

  <section class="card card-back" aria-label="Business card back">
    <p class="back-brand">Quorvane Capital</p>
    <p class="tagline">Diversified Crypto Investment Funds</p>
  </section>
</main>
</body>
</html>
```